Movie Poster - Two Types - Independent Jazz Documentary

Need a better movie poster than the one we currently use which can be viewed on our website: www.carlmodryhourslost.com
Two posters are needed: Standard regular movie poster (ideal image size of 2025 x 3000 px) and a smaller version for on-demand platforms such as Vidorra (600 x 600 px). This is not set in stone, so we have flexibility on the sizing. We just need a good standard type size and a smaller design version.
If possible, try to use the existing poster we have or stick to the same theme. Winning designer may be asked for some follow-up work such as DVD label which I will gladly pay for on top of what is paid for the posters.
Updates
Ideal image sizes for this project would be:2025 x 3000 px for the standard movie poster 600 x 600 px for the Vidorra imageThese are recommended image sizes, not a must. We can work around most image sizes as long as we can get good rendering on different devices and paper print outs. Added Sunday, April 3, 2016
A few of the designers have used four film festival images which adds more power to the poster. I have uploaded three image files that you may want to use in addition to what has been provided in the powerpoint slide deck: Quillmere Film Festival, Tall Fern Film Festival (image 1 of 2), and Tall Fern Film Festival (image 2 of 2). A few designers submitted two posters, one which builds on the original poster which has been included + a more creative poster that is very different. I would suggest that you consider submitting two posters to increase your chances of placing for 1st, 2nd, or 3rd. So far, everyone has produced some really nice stuff. Also keep in mind that I will provide some add on work for whoever wins 1st, 2nd or 3rd: DVD Insert Artwork and Social Media Headers. Added Thursday, April 7, 2016
For the few designers who were eliminated and may want to take another shot, I posted a Movie Poster Example of what we are looking for. If you got a five star rating on your design, then you should focus only on some minor changes. If you got a Favorite, then you are exactly hitting the bulls eye and you can just sit back and wait for the contest to end. Added Friday, April 8, 2016
Target Market(s)
Jazz music audience which may attend film festivals
Industry/Entity Type
Movie
Requirements
Must have
- Image of the jazz pianist Carl Modry
- Include the name of the movie producer who is Norman Tallick
- Indicate this is a Documentary Film about the life and music of Carl Modry
- Include references to film festivals where this film has been shown: PLAVFest 2016, Quillmere Film Festival, Tall Fern Film Festival, Reel N Jive Film Festival
Nice to have
- Reference to the film's website: www.carlmodryhourslost.com
- Reference to the fact that this film took eight years to complete and include at least 40 interviews
Should not have
- Do not make the text too small since the image file may get downsized and placed on different internet platforms for promotion (such as FlickTo)

```html
<!DOCTYPE html>
<html lang="en">
<head>
<meta charset="utf-8">
<title>Hours Lost – Carl Modry</title>
<link rel="stylesheet" href="https://fonts.googleapis.com/css2?family=Bebas+Neue&display=swap">
<style>
  :root {
    --paper: #ffffff;
    --ink: #111111;
    --key-black: #141414;
    --key-line: #cfe2ea;
    --photo-dark: #1f4d63;
    --photo-mid: #7fa9b8;
    --photo-light: #e6f0f2;
    --face-tone: #2e5a6b;
    --festival-ink: #22343c;
    --scene-dark: #3a4d55;
  }
  * { margin: 0; padding: 0; box-sizing: border-box; }
  html, body { width: 810px; height: 1200px; overflow: hidden; background: var(--paper); }
  .poster {
    position: relative; width: 810px; height: 1200px; overflow: hidden;
    background: var(--paper);
    font-family: "Bebas Neue", "Oswald", sans-serif;
    color: var(--ink);
  }
  .backdrop {
    position: absolute; left: 9px; top: 0; width: 330px; height: 1141px;
    background: linear-gradient(180deg, var(--photo-dark) 0%, var(--photo-mid) 40%, #a9c6cd 72%, var(--photo-light) 100%);
  }
  .portrait {
    position: absolute; left: 9px; top: 150px; width: 330px; height: 760px;
    background:
      radial-gradient(ellipse 62% 48% at 40% 55%, rgba(46,90,107,0.85), rgba(46,90,107,0.35) 60%, transparent 80%),
      radial-gradient(ellipse 40% 20% at 55% 12%, rgba(230,240,242,0.45), transparent 70%);
  }
  .pianist-scene {
    position: absolute; left: 150px; top: 975px; width: 180px; height: 80px;
    background: linear-gradient(180deg, rgba(58,77,85,0.75), rgba(58,77,85,0.35));
    border-radius: 4px;
  }
  .keyboard { position: absolute; left: 339px; top: 0; width: 461px; height: 1141px; }
  .key-line { position: absolute; left: 0; right: 0; height: 3px; background: var(--key-line); }
  .black-key { position: absolute; left: 152px; right: 0; height: 74px; background: var(--key-black); }
  .tagline {
    position: absolute; right: 481px; top: 20px; text-align: right;
    color: var(--paper); font-size: 56px; line-height: 65px;
  }
  .tagline .amp { font-size: 28px; vertical-align: middle; }
  .festivals {
    position: absolute; right: 488px; top: 812px; list-style: none;
    text-align: right; color: var(--festival-ink);
    font-size: 16px; line-height: 24px; letter-spacing: 0.5px;
  }
  .festivals li::before {
    content: ""; display: inline-block; width: 8px; height: 8px;
    border-radius: 50%; background: var(--festival-ink);
    margin-right: 6px; vertical-align: 2px;
  }
  .title-top {
    position: absolute; right: 24px; top: 640px; color: var(--paper);
    font-size: 56px; line-height: 1;
  }
  .title-bottom { position: absolute; right: 24px; top: 728px; font-size: 50px; line-height: 1; }
  .subject {
    position: absolute; right: 24px; top: 792px; text-align: right;
    font-size: 140px; line-height: 138px;
  }
  .credit-label { position: absolute; right: 24px; top: 1064px; font-size: 24px; letter-spacing: 0.5px; }
  .credit-name { position: absolute; right: 24px; top: 1090px; font-size: 44px; letter-spacing: 1px; }
  .site-band {
    position: absolute; left: 9px; top: 1143px; width: 791px; height: 38px;
    background: var(--key-black); color: var(--paper);
    font-size: 26px; letter-spacing: 3px; text-align: center; line-height: 40px;
  }
</style>
</head>
<body>
<div class="poster">
  <div class="backdrop"></div>
  <div class="portrait" role="img" aria-label="Blue-toned portrait of pianist Carl Modry in glasses, blended with a collage of interview subjects"></div>
  <div class="pianist-scene" role="img" aria-label="Silhouette of a pianist seated at a grand piano"></div>

  <div class="keyboard">
    <div class="key-line" style="top:149px"></div>
    <div class="key-line" style="top:278px"></div>
    <div class="key-line" style="top:407px"></div>
    <div class="key-line" style="top:536px"></div>
    <div class="key-line" style="top:670px"></div>
    <div class="key-line" style="top:803px"></div>
    <div class="key-line" style="top:932px"></div>
    <div class="black-key" style="top:117px"></div>
    <div class="black-key" style="top:377px"></div>
    <div class="black-key" style="top:636px"></div>
  </div>

  <div class="tagline">THE<br>LIFE <span class="amp">&amp;</span> MUSIC<br>OF<br>CARL<br>MODRY</div>

  <ul class="festivals">
    <li>Quillmere Film Festival 2015</li>
    <li>Reel N Jive Film Festival</li>
    <li>PLAVFest 2016</li>
    <li>Tall Fern Film Festival 2016</li>
    <li>Beacon Documentary Awards 2015</li>
  </ul>

  <div class="title-top">HOURS</div>
  <div class="title-bottom">LOST</div>
  <div class="subject">CARL<br>MODRY</div>
  <div class="credit-label">A DOCUMENTARY FILM PRODUCED BY</div>
  <div class="credit-name">NORMAN TALLICK</div>
  <div class="site-band">WWW.CARLMODRYHOURSLOST.COM</div>
</div>
</body>
</html>
```